Postcard Flyer For Plumbing Company

We are a p[professional plumbing company in NSW that carry out plumbing, electrical and hot water system work.
i want to send a postcard size flyer 105mm x 148mm to our clients to offer $xx off their next job they book with us.
The front of the flyer needs to say.... Feel The Love WIth $35 Off your Next Job. It needs to include a section where their name and postal address can go (74mm W x 24mm H) on the left hand side of the bottom of the flyer - refer attached example.
The other side of the flyer needs to have a section for text, the offer ($35 or $xx what they get off their next job) and also can use the tag line... Call 1 Number for The Best In 3 Trades - Plumbing, Hot Water & Electrical.
Plumbing, hot water and electrical pictures/icons can be used.
I want the flyer to stand out, use the corporate colours and be modern whilst letting them know that they can use this voucher on their next job.
Refer attachments.

Target Market(s)

Homeowners and our existing clients

Industry/Entity Type

Plumbing

Font styles to use
Serif

Colors
0255a3
ec1f27
ffffff
d3d3d3

Requirements
Must have
• Corporate colours and logos
• Red Colour:
• C=0
• M=100
• Y=100
• K=0
• Blue Colour
• C= 100
• M=66
• Y=0
• K=2
• Grey Colour
• C= 26
• M=21
• Y=19
• K=0
Nice to have
• predominately white background
Should not have
• Black background and lots of black.

```html
<!DOCTYPE html>
<html lang="en">
<head>
<meta charset="utf-8">
<title>Kestrel Contracting – $35 Off Postcard</title>
<link rel="stylesheet" href="https://fonts.googleapis.com/css2?family=Lato:wght@300;400;700;900&family=Oswald:wght@400&display=swap">
<style>
  :root{
    --navy:#2f3894;
    --blue:#0a5bb5;
    --red:#e1262d;
    --charcoal:#3c3c41;
    --ink:#222226;
    --rule:#c4c4c4;
    --white:#ffffff;
    --backdrop:#e8e8e8;
  }
  *{box-sizing:border-box;margin:0;padding:0}
  html,body{width:930px;height:1200px;overflow:hidden}
  body{background:var(--backdrop);font-family:"Lato",sans-serif;position:relative}
  .card{position:absolute;left:65px;width:800px;height:567px;background:var(--white);overflow:hidden;box-shadow:0 4px 14px rgba(0,0,0,.25)}
  .card--front{top:22px}
  .card--back{top:611px}
  .layer{position:absolute;inset:0}
  .abs{position:absolute}

  /* front */
  .hero-photo{left:0;top:0;width:800px;height:360px;background:linear-gradient(100deg,#d9dde3 0%,#eef0f2 35%,#b9c0c9 60%,#6f86b3 85%,#d8c2b0 100%)}
  .brand-panel{left:37px;top:0;width:220px;height:360px;background:var(--white)}
  .brand-name{left:37px;width:220px;text-align:center;color:var(--navy);font-weight:900;line-height:1}
  .front-brand{top:52px;font-size:32px;letter-spacing:1px}
  .front-brand span{display:block;font-size:21px;letter-spacing:.5px;margin-top:6px}
  .front-headline{left:37px;top:158px;width:220px;text-align:center;color:var(--navy);font-size:17px;line-height:23px}
  .feature-circle{left:23px;top:246px;width:248px;height:248px;border-radius:50%;background:var(--white);box-shadow:0 3px 10px rgba(0,0,0,.35);padding:6px}
  .feature-circle .ring{width:100%;height:100%;border-radius:50%;border:6px solid var(--navy);padding:4px;background:var(--white)}
  .feature-circle .photo{width:100%;height:100%;border-radius:50%;background:radial-gradient(circle at 40% 30%,#f4f4f4,#c9ccd1 55%,#c98b62 80%,#9aa0a8)}
  .trade{width:122px;top:345px;text-align:center}
  .trade .badge{width:122px;height:122px;border-radius:50%;border:3px solid var(--red);padding:3px;background:var(--white)}
  .trade .photo{width:100%;height:100%;border-radius:50%}
  .trade .label{color:var(--white);font-size:17px;margin-top:14px}
  .trade--plumbing{left:329px}
  .trade--plumbing .photo{background:radial-gradient(circle at 45% 40%,#f3f3f3,#b8bdc4 60%,#7d8590)}
  .trade--hotwater{left:489px}
  .trade--hotwater .photo{background:radial-gradient(circle at 50% 45%,#e8e0cf,#aab0b8 55%,#6c737c)}
  .trade--electrical{left:646px}
  .trade--electrical .photo{background:radial-gradient(circle at 50% 50%,#eaeaea,#9aa1aa 60%,#4e555e)}
  .front-footer{left:0;top:514px;width:800px;height:53px;display:flex;align-items:center;justify-content:space-between;padding:0 22px;color:var(--white);font-size:23px}
  .contact{display:flex;align-items:center;gap:6px}
  .contact svg{flex:none}

  /* back */
  .back-brand{left:20px;top:24px;width:auto;text-align:left;font-size:42px;letter-spacing:1px}
  .back-brand span{display:block;font-size:28px;margin-top:6px}
  .trades-line{left:20px;top:139px;font-weight:700;font-size:17px;color:var(--ink)}
  .back-heading{left:20px;top:180px;font-size:22px;line-height:28px;color:var(--ink)}
  .benefits{left:20px;top:250px;list-style:none;font-weight:300;font-size:16.5px;color:var(--ink)}
  .benefits li{display:flex;align-items:center;gap:5px;height:26.5px}
  .offer{left:59px;top:366px;width:300px;height:58px;background:var(--red);border:3px solid var(--charcoal);color:var(--white);font-family:"Oswald",sans-serif;font-size:31px;display:flex;align-items:center;justify-content:center;letter-spacing:.3px}
  .call-block{left:28px;top:456px;color:var(--white);font-size:18px;line-height:23px}
  .call-block .contact{font-size:22px;margin-top:10px}
  .stamp{left:643px;top:35px;width:119px;height:96px;border:1.5px solid var(--rule)}
  .address-line{left:495px;width:266px;height:0;border-top:1.5px solid var(--rule)}
  .back-web{left:435px;top:506px;font-size:22px;color:var(--ink)}
</style>
</head>
<body>

<section class="card card--front" aria-label="Postcard front">
  <div class="abs hero-photo" role="img" aria-label="Photo of a smiling plumber repairing pipes under a sink"></div>
  <div class="abs brand-panel"></div>

  <svg class="layer" width="800" height="567" viewBox="0 0 800 567" aria-hidden="true">
    <path d="M0 300 C120 334 260 350 380 340 C520 328 680 308 800 322 L800 514 L0 514 Z" fill="var(--navy)"/>
    <path d="M0 292 C120 326 260 342 380 332 C520 320 680 300 800 314" fill="none" stroke="var(--white)" stroke-width="5"/>
    <path d="M0 298 C120 332 260 348 380 338 C520 326 680 306 800 320" fill="none" stroke="var(--red)" stroke-width="6"/>
    <rect x="0" y="511" width="800" height="3" fill="var(--white)"/>
    <rect x="0" y="514" width="800" height="53" fill="var(--charcoal)"/>
  </svg>

  <p class="abs brand-name front-brand">KESTREL<span>Contracting</span></p>
  <p class="abs front-headline">Feel The Love With $35<br>Off your Next Job</p>

  <div class="abs feature-circle">
    <div class="ring"><div class="photo" role="img" aria-label="Photo of copper pipes, tap fittings, a spanner and building plans"></div></div>
  </div>

  <div class="abs trade trade--plumbing">
    <div class="badge"><div class="photo" role="img" aria-label="Photo of chrome sink waste pipes"></div></div>
    <p class="label">Plumbing</p>
  </div>
  <div class="abs trade trade--hotwater">
    <div class="badge"><div class="photo" role="img" aria-label="Photo of hot water taps and brass fittings"></div></div>
    <p class="label">Hot Water</p>
  </div>
  <div class="abs trade trade--electrical">
    <div class="badge"><div class="photo" role="img" aria-label="Photo of an electrical switchboard with circuit breakers"></div></div>
    <p class="label">Electrical</p>
  </div>

  <div class="abs front-footer">
    <span class="contact">
      <svg width="22" height="22" viewBox="0 0 24 24" aria-hidden="true"><path d="M6.6 10.8a15.1 15.1 0 0 0 6.6 6.6l2.2-2.2a1 1 0 0 1 1-.25 11.4 11.4 0 0 0 3.6.57 1 1 0 0 1 1 1V20a1 1 0 0 1-1 1A17 17 0 0 1 3 4a1 1 0 0 1 1-1h3.5a1 1 0 0 1 1 1c0 1.25.2 2.45.57 3.57a1 1 0 0 1-.25 1z" fill="currentColor"/></svg>
      1800 555 012
    </span>
    <span class="contact">
      <svg width="20" height="20" viewBox="0 0 24 24" aria-hidden="true"><g fill="none" stroke="currentColor" stroke-width="2"><circle cx="12" cy="12" r="10"/><ellipse cx="12" cy="12" rx="4" ry="10"/><path d="M2 12h20M4 7h16M4 17h16"/></g></svg>
      www.kestrelcontracting.com.au
    </span>
  </div>
</section>

<section class="card card--back" aria-label="Postcard back">
  <svg class="layer" width="800" height="567" viewBox="0 0 800 567" aria-hidden="true">
    <polygon points="0,443 392,443 354,550 0,550" fill="var(--charcoal)"/>
    <polygon points="80,424 104,424 84,443" fill="var(--charcoal)"/>
    <path d="M325 0 C420 120 442 330 336 567" fill="none" stroke="var(--blue)" stroke-width="11"/>
  </svg>

  <div class="abs" style="left:336px;top:26px;width:66px;height:66px;border-radius:50%;background:radial-gradient(circle at 45% 40%,#dfe6ef,#1d63b8 70%);border:3px solid var(--white);box-shadow:0 2px 5px rgba(0,0,0,.3)" role="img" aria-label="Plumbing pipe icon"></div>
  <div class="abs" style="left:366px;top:118px;width:66px;height:66px;border-radius:50%;background:radial-gradient(circle at 50% 45%,#f0f0f0,#9ea3aa 75%);border:3px solid var(--white);box-shadow:0 2px 5px rgba(0,0,0,.3)" role="img" aria-label="Hot water tap icon"></div>
  <div class="abs" style="left:385px;top:214px;width:66px;height:66px;border-radius:50%;background:radial-gradient(circle at 50% 45%,#fafafa 0 18%,var(--red) 45%);border:3px solid var(--white);box-shadow:0 2px 5px rgba(0,0,0,.3)" role="img" aria-label="Light bulb icon"></div>

  <p class="abs brand-name back-brand">KESTREL<span>Contracting</span></p>
  <p class="abs trades-line">Plumbing • Electrical • Hot Water</p>
  <h2 class="abs back-heading" style="font-weight:400">Fast Reliable Plumbing and<br>Electrical Services.</h2>

  <ul class="abs benefits">
    <li><svg width="14" height="14" viewBox="0 0 14 14" aria-hidden="true"><rect x="1" y="2" width="11" height="11" rx="2" fill="none" stroke="var(--red)" stroke-width="1.8"/><path d="M3.5 7.5l2.5 2.5 7-8" fill="none" stroke="var(--red)" stroke-width="2.2"/></svg>Servicing Sydney for over 30yrs</li>
    <li><svg width="14" height="14" viewBox="0 0 14 14" aria-hidden="true"><rect x="1" y="2" width="11" height="11" rx="2" fill="none" stroke="var(--red)" stroke-width="1.8"/><path d="M3.5 7.5l2.5 2.5 7-8" fill="none" stroke="var(--red)" stroke-width="2.2"/></svg>Offering expert Advice and real solutions</li>
    <li><svg width="14" height="14" viewBox="0 0 14 14" aria-hidden="true"><rect x="1" y="2" width="11" height="11" rx="2" fill="none" stroke="var(--red)" stroke-width="1.8"/><path d="M3.5 7.5l2.5 2.5 7-8" fill="none" stroke="var(--red)" stroke-width="2.2"/></svg>100% Satisfaction and Dependability at a Fair Price</li>
    <li><svg width="14" height="14" viewBox="0 0 14 14" aria-hidden="true"><rect x="1" y="2" width="11" height="11" rx="2" fill="none" stroke="var(--red)" stroke-width="1.8"/><path d="M3.5 7.5l2.5 2.5 7-8" fill="none" stroke="var(--red)" stroke-width="2.2"/></svg>All Staff are Fully Trained in Safety</li>
  </ul>

  <p class="abs offer">$35 OFF YOUR NEXT JOB</p>

  <div class="abs call-block">
    <p>Call 1 Number for The Best In 3 Trades<br>Plumbing, Hot Water &amp; Electrical.</p>
    <p class="contact">
      <svg width="21" height="21" viewBox="0 0 24 24" aria-hidden="true"><path d="M6.6 10.8a15.1 15.1 0 0 0 6.6 6.6l2.2-2.2a1 1 0 0 1 1-.25 11.4 11.4 0 0 0 3.6.57 1 1 0 0 1 1 1V20a1 1 0 0 1-1 1A17 17 0 0 1 3 4a1 1 0 0 1 1-1h3.5a1 1 0 0 1 1 1c0 1.25.2 2.45.57 3.57a1 1 0 0 1-.25 1z" fill="currentColor"/></svg>
      1800 555 012
    </p>
  </div>

  <div class="abs stamp"></div>
  <div class="abs address-line" style="top:252px"></div>
  <div class="abs address-line" style="top:293px"></div>
  <div class="abs address-line" style="top:333px"></div>
  <div class="abs address-line" style="top:373px"></div>
  <div class="abs address-line" style="top:413px"></div>

  <p class="abs back-web contact">
    <svg width="18" height="18" viewBox="0 0 24 24" aria-hidden="true"><g fill="none" stroke="currentColor" stroke-width="2"><circle cx="12" cy="12" r="10"/><ellipse cx="12" cy="12" rx="4" ry="10"/><path d="M2 12h20M4 7h16M4 17h16"/></g></svg>
    www.kestrelcontracting.com.au
  </p>
</section>

</body>
</html>
```